business card design - photography

I am a fine art photographer. I would like to approach galleries to exhibit my work and need a business card.

The card should convey creativity and simplicity.
I would like a double sided card.

Some options:
1. An all white card with raised or embossed text or design to create a tactile finish.
2. a white and dark grey design would also work well.
3. Would be great to use my name as part of the design but not essential.
4. My name and title on the front, other details on the back of card.

The final design should be simple, minimal, elegant and innovative.
Being minimal, it will be more about texture, text size and placement.

examples of designs I would prefer provided here:
http://plimvarka.com/ideas/40-quiet-and-refined-card-layouts

I'm also open to other designs that may be unusual and unique.

Love this:
http://www.snapvelo.com/pics/morningverselog/583014927
Updates

I have uploaded a psd file after playing around in photoshop with various fonts.  I like the font (which I downloaded from glyphmorra.com called Arual) but the design probably needs some refining.  I hope this helps.  If you'd like me to change the format of the file, please let me know.

Ilvane

Target Market(s)

Art Gallery owners/administrators and customers.

Industry/Entity Type

Business

Requirements
Must have
• A unique look.

Matte, silky finish or heavy textured stock. Double-sided card.

Front:
my name
photography by

Back:
phone no
email
web address
Nice to have
• Letterpress
embrossed
Clean fonts
Should not have
• Do not use illustrations of cameras or lenses.
No frames around the card edge.

```html
<!DOCTYPE html>
<html lang="en">
<head>
<meta charset="utf-8">
<title>Ilvane Kessby Photography – Business Card</title>
<link rel="stylesheet" href="https://fonts.googleapis.com/css2?family=Zilla+Slab:wght@700&family=Raleway:wght@400&family=Questrial&display=swap">
<style>
  :root {
    --ink-dark: #1b1f20;
    --paper: #ffffff;
    --text-dark: #1a1a1a;
  }
  html, body {
    margin: 0;
    padding: 0;
    width: 1200px;
    height: 1033px;
    overflow: hidden;
    background: var(--paper);
  }
  .card {
    position: relative;
    width: 1200px;
    height: 1033px;
    background: var(--paper);
  }
  .brand-band {
    position: absolute;
    left: 0;
    top: 0;
    width: 1200px;
    height: 516px;
    background: var(--ink-dark);
  }
  .brand-name {
    position: absolute;
    right: 33px;
    top: 302px;
    margin: 0;
    font-family: "Zilla Slab", "Roboto Slab", serif;
    font-weight: 700;
    font-size: 140px;
    line-height: 1;
    letter-spacing: -2px;
    color: var(--paper);
    white-space: nowrap;
  }
  .brand-title {
    position: absolute;
    right: 30px;
    top: 474px;
    margin: 0 -22px 0 0;
    font-family: "Raleway", sans-serif;
    font-weight: 400;
    font-size: 27px;
    line-height: 1;
    letter-spacing: 22.5px;
    color: var(--paper);
    white-space: nowrap;
  }
  .contact-list {
    position: absolute;
    left: 35px;
    top: 862px;
    margin: 0;
    padding: 0;
    list-style: none;
  }
  .contact-item {
    display: flex;
    align-items: center;
    height: 49px;
    font-family: "Questrial", sans-serif;
    font-size: 29px;
    letter-spacing: -0.5px;
    color: var(--text-dark);
  }
  .contact-icon {
    width: 28px;
    height: 28px;
    margin-right: 11px;
    flex: none;
  }
</style>
</head>
<body>
  <div class="card">
    <header class="brand-band">
      <h1 class="brand-name">Ilvane Kessby</h1>
      <p class="brand-title">PHOTOGRAPHY</p>
    </header>

    <ul class="contact-list">
      <li class="contact-item">
        <svg class="contact-icon" viewBox="0 0 28 28" aria-hidden="true">
          <path d="M2 11 Q14 3 26 11 L24 14 L19 12 L19 10 Q14 8 9 10 L9 12 L4 14 Z" fill="var(--text-dark)"/>
          <path d="M6 16 L10 12 L18 12 L22 16 L22 23 L6 23 Z" fill="var(--text-dark)"/>
          <circle cx="14" cy="18" r="2.5" fill="var(--paper)"/>
        </svg>
        <span class="contact-text">0491 572 318</span>
      </li>
      <li class="contact-item">
        <svg class="contact-icon" viewBox="0 0 28 28" aria-hidden="true">
          <rect x="1" y="7" width="26" height="16" fill="var(--text-dark)"/>
          <path d="M2 8 L14 17 L26 8" fill="none" stroke="var(--paper)" stroke-width="1.4"/>
          <path d="M2 22 L11 14 M26 22 L17 14" fill="none" stroke="var(--paper)" stroke-width="1.2"/>
        </svg>
        <span class="contact-text">ikessby@mailvero.com</span>
      </li>
      <li class="contact-item">
        <svg class="contact-icon" viewBox="0 0 28 28" aria-hidden="true">
          <g fill="none" stroke="var(--text-dark)" stroke-width="1.5">
            <circle cx="14" cy="14" r="11"/>
            <ellipse cx="14" cy="14" rx="5" ry="11"/>
            <line x1="3" y1="14" x2="25" y2="14"/>
            <path d="M5 8 H23 M5 20 H23"/>
            <line x1="14" y1="3" x2="14" y2="25"/>
          </g>
        </svg>
        <span class="contact-text">www.ilvanekessby.com</span>
      </li>
    </ul>
  </div>
</body>
</html>
```